Boutique High End Custom Furniture Store, Client Appreciation Card

We are looking to create a 5 x 7 card for our best clients that offer a 15% discount on their next furniture purchase. We would like to use both sides, full colour.

We are a high-end boutique furniture store located in Calgary, AB, Canada.

I have attached a card we did for our grand reopening that we like -- it's fresh with lots of white space. I have attached the image we used as well as a possible second image of furniture.

I have also attached other examples -- all seem fresh and clean with a layer of luxury.

I have attached all versions of our logo in an EPS file.

Target Market(s)

High disposable income, women over 40 who love style, contemporary design and fine art. Think Lina Morrow, Finch Allard, Vera Quill perfume and http://www.marlowbey.example/

Industry/Entity Type

Boutique

Font styles to use
Sans Serif
Script

Colors
33a6d7
0592cd
85cae6
eda3c7
e667a6

Requirements
Must have
• Must be colour on both side (one side logo perhaps), the other side has content? Card needs to be 5 x 7 (either orientation is okay). Card needs to be fresh, stylish and current with the use of colour i.e. not all black and white. Logo needs to be prominent on either side.
• Please also have a look at our website.
Should not have
• Should not feel traditional or dated but at the same time not too playful so that it looks unprofessional. We are not "Hal's discount Sofas"!

```html
<!DOCTYPE html>
<html lang="en">
<head>
<meta charset="utf-8">
<title>Alder Maison – Client Appreciation Card</title>
<link rel="stylesheet" href="https://fonts.googleapis.com/css2?family=Arimo:wght@400;700&family=Cormorant+Garamond:wght@500&display=swap">
<style>
  :root {
    --stage: #ddd8d8;
    --pink: #e667a6;
    --white: #ffffff;
    --ink: #231f20;
    --grey-text: #4a4a4a;
    --sans: "Arimo", Arial, sans-serif;
    --serif: "Cormorant Garamond", Georgia, serif;
  }
  * { box-sizing: border-box; margin: 0; padding: 0; }
  html, body { width: 1200px; height: 1200px; overflow: hidden; }
  body { background: var(--stage); position: relative; font-family: var(--sans); }

  .card {
    position: absolute; top: 238px; width: 516px; height: 722px;
    overflow: hidden; box-shadow: 4px 6px 8px rgba(0,0,0,0.28);
  }
  .card--front { left: 58px; background: var(--white); }
  .card--back { left: 630px; }

  /* front */
  .hero-photo {
    position: absolute; left: 0; top: 0; width: 516px; height: 558px;
    background: linear-gradient(180deg, #f4f3f1 0%, #e6e3df 42%, #a9a39c 70%, #6f6b66 100%);
  }
  .offer-badge {
    position: absolute; left: 323px; top: 121px; width: 166px; height: 166px;
    border-radius: 50%; background: var(--pink); color: var(--white);
    font-family: var(--serif); text-align: center;
    font-variant-numeric: lining-nums;
  }
  .offer-badge__value { position: absolute; left: 0; right: 0; top: 44px; font-size: 58px; line-height: 1; }
  .offer-badge__label { position: absolute; left: 0; right: 0; top: 101px; font-size: 24px; letter-spacing: 1px; line-height: 1; }

  .headline {
    position: absolute; left: 52px; top: 286px; color: var(--white);
    font-size: 42px; font-weight: 700; line-height: 1;
  }
  .subhead {
    position: absolute; left: 52px; top: 335px; color: var(--white);
    font-size: 29px; line-height: 1; white-space: nowrap;
  }
  .subhead strong { font-weight: 700; }

  .brand-panel {
    position: absolute; left: 0; top: 484px; width: 340px; height: 74px;
    background: rgba(255,255,255,0.78);
  }
  .brand-name {
    color: var(--ink); font-weight: 400; letter-spacing: 1px;
    line-height: 1; white-space: nowrap;
  }
  .brand-panel .brand-name { position: absolute; left: 52px; top: 13px; font-size: 33px; }
  .brand-tagline {
    color: var(--ink); letter-spacing: 2px; line-height: 1; white-space: nowrap;
  }
  .brand-panel .brand-tagline { position: absolute; left: 54px; top: 52px; font-size: 14px; }

  .about {
    position: absolute; left: 52px; top: 576px; width: 416px;
    color: var(--pink); font-size: 14px; line-height: 17.6px; text-align: justify;
  }
  .fine-print {
    position: absolute; left: 52px; top: 637px; color: var(--grey-text);
    font-size: 12.3px; white-space: nowrap;
  }
  .contact-band {
    position: absolute; left: 0; top: 666px; width: 516px; height: 56px;
    background: var(--pink); color: var(--white);
  }
  .contact-band__mark {
    position: absolute; left: 62px; top: 12px; width: 30px; height: 30px;
    border: 2px solid var(--white);
  }
  .contact-band__lines {
    position: absolute; left: 126px; top: 10px; font-size: 13px; line-height: 18px; white-space: nowrap;
  }
  .sep { margin: 0 8px; }

  /* back */
  .back-pattern { position: absolute; inset: 0; background: var(--pink); }
  .logo-frame {
    position: absolute; left: 128px; top: 162px; width: 261px; height: 258px;
    background: var(--white); border: 3px solid var(--ink);
  }
  .logo-frame::after {
    content: ""; position: absolute; inset: 3px; border: 1px solid var(--ink);
  }
  .logo-frame__mark {
    position: absolute; left: 114px; top: 68px; width: 28px; height: 28px;
    border: 2px solid var(--ink);
  }
  .logo-frame .brand-name { position: absolute; left: 0; right: 0; top: 128px; text-align: center; font-size: 30px; }
  .logo-frame .brand-tagline { position: absolute; left: 0; right: 0; top: 169px; text-align: center; font-size: 13px; }
  .back-contact {
    position: absolute; left: 0; right: 0; top: 553px; text-align: center;
    color: var(--white); font-size: 13.4px; line-height: 20.7px; font-style: normal;
  }
</style>
</head>
<body>

<section class="card card--front">
  <div class="hero-photo" role="img" aria-label="Photo of a grey sideboard with a yellow vase of white lilies, books, a small sculpture and an upholstered bench"></div>

  <div class="offer-badge">
    <div class="offer-badge__value">15%</div>
    <div class="offer-badge__label">OFF</div>
  </div>

  <h1 class="headline">Our Gift to You</h1>
  <p class="subhead">Enjoy <strong>15%</strong> off at Alder Maison</p>

  <div class="brand-panel">
    <div class="brand-name">Alder Maison</div>
    <div class="brand-tagline">Calgary Home Atelier</div>
  </div>

  <p class="about">Alder Maison is a unique boutique custom furniture store offering a wide selection of furniture, rugs, bedding, lighting, window coverings, accessories and interior design services.</p>
  <p class="fine-print">Offer is good for one-time use and cannot be combined with other offers.</p>

  <footer class="contact-band">
    <div class="contact-band__mark"></div>
    <div class="contact-band__lines">
      <div>482 Harlow St SW, Calgary AB<span class="sep">|</span>403.555.0142</div>
      <div>info@aldermaison.ca<span class="sep">|</span>aldermaison.ca</div>
    </div>
  </footer>
</section>

<section class="card card--back">
  <div class="back-pattern" role="img" aria-label="Pink background with fine white line drawings of peonies and leaves"></div>

  <div class="logo-frame">
    <div class="logo-frame__mark"></div>
    <div class="brand-name">Alder Maison</div>
    <div class="brand-tagline">Calgary Home Atelier</div>
  </div>

  <address class="back-contact">
    482 Harlow St SW, Calgary AB<br>
    403.555.0142<br>
    info@aldermaison.ca<br>
    aldermaison.ca
  </address>
</section>

</body>
</html>
```